Salmon Shop that sells both wholesale and retail salmon in a variety of ways.

"Harbour Fillet Co" is a business that is selling atlantic salmon in every way possible. We will be a salmon butcher to the public for retail purchase and we will also be out and about trying to sell our products to restaurants cafes and any other wholesale way. Our product is from Tasmania but we will be trading on the Sunshine Coast. The shop design has an urban, rustic feel and very much about the product. One of the owners has worked on salmon farms for 15 years and we want it to be very specialised and quality. I have nothing to offer you to help with this design....I would like both a salmon on the card, not sure if image or silohette is best and would like the other side to have a fillet with a tag of some sort. We are looking for a logo also. Use a photo of an Atlantic Salmon, Atlantic Salmon have two fins along the back.
Updates

Project Deadline Extended Reason: I am extending the deadline as I have still not got exactly what I want. All designers have added something great to what I am after and I just need someone to pull it all together. I have put in a new brief with a sketched image to help so we can get this perfect. Please read all the instructions. Thank you Added Monday, February 16, 2015

Target Market(s)

Restaurants, cafes

Industry/Entity Type

Retail

Contact Information for Business Card

Harbour Fillet Co (Not to have "Shop" at the end.Shop 12/130-164 Brisbane RdMooloolaba 4557

Colors
1c66ab

Requirements
Must have
• logo for harbour fillet Co with the S being salmon fillet of fresh salmon on white platemap of tasmaniasepia /black and white image of atlantic salmon
Nice to have
• fillet of salmonmap of tasmaniasalmon
Should not have
• Not Shop at the end.

```html
<!DOCTYPE html>
<html lang="en">
<head>
<meta charset="utf-8">
<title>Harbour Fillet Co – Business Card</title>
<link rel="stylesheet" href="https://fonts.googleapis.com/css2?family=Open+Sans:wght@300;700&display=swap">
<style>
  :root {
    --backdrop: #dedad9;
    --brand-blue: #1c66ab;
    --logo-blue: #3a5f98;
    --wood-light: #9c9894;
    --wood-mid: #85817d;
    --wood-dark: #6c6864;
    --plank-line: rgba(50, 46, 42, 0.55);
    --panel-white: #f4f4f4;
    --panel-grey: #d9d9d9;
    --ink-dark: #3a3a3a;
    --ink-light: #ffffff;
    --fillet: #ec8e5c;
    --fillet-deep: #d9683a;
    --lemon: #f4cf3c;
    --greens: #4f8d36;
    --fish-silver: #c9ccd0;
    --fish-dark: #7b8088;
  }
  html, body {
    margin: 0;
    width: 1200px;
    height: 800px;
    overflow: hidden;
    background: var(--backdrop);
    font-family: "Open Sans", Arial, sans-serif;
  }
  .canvas {
    position: relative;
    width: 1200px;
    height: 800px;
  }
  .card {
    position: absolute;
    top: 90px;
    width: 360px;
    height: 620px;
    overflow: hidden;
    box-shadow: 0 6px 18px rgba(0, 0, 0, 0.18);
  }
  .card--front { left: 200px; }
  .card--back  { left: 640px; }

  .wood {
    position: absolute;
    background:
      repeating-linear-gradient(0deg, transparent 0 38px, var(--plank-line) 38px 40px),
      linear-gradient(90deg, var(--wood-light), var(--wood-mid) 45%, var(--wood-dark) 100%);
  }
  .card--front .wood { inset: 0; }

  /* front */
  .front-logo {
    position: absolute;
    top: 28px;
    right: 34px;
    z-index: 2;
    writing-mode: vertical-rl;
    font-weight: 700;
    font-size: 32px;
    line-height: 1.1;
    color: var(--logo-blue);
    letter-spacing: 1px;
  }
  .contact {
    position: absolute;
    top: 36px;
    right: 118px;
    z-index: 2;
    writing-mode: vertical-rl;
    color: var(--ink-light);
    font-weight: 300;
    font-size: 12px;
    line-height: 18px;
    margin: 0;
    padding: 0;
    list-style: none;
  }
  .contact__name {
    font-size: 22px;
    line-height: 32px;
  }
  .contact li { display: flex; align-items: center; gap: 5px; }
  .contact svg { width: 11px; height: 11px; flex: none; }

  .dish-photo {
    position: absolute;
    left: -10px;
    right: -10px;
    bottom: -10px;
    height: 360px;
    border: 10px solid var(--panel-white);
    border-radius: 50% 50% 0 0 / 36% 36% 0 0;
    background:
      radial-gradient(circle at 30% 45%, var(--lemon) 0 14%, transparent 15%),
      radial-gradient(circle at 62% 55%, var(--fillet) 0 28%, transparent 29%),
      radial-gradient(circle at 75% 80%, var(--fillet-deep) 0 22%, transparent 23%),
      linear-gradient(160deg, var(--greens), var(--fillet) 55%, var(--panel-white));
  }

  /* back */
  .info-panel {
    position: absolute;
    top: 0; bottom: 0; left: 0;
    width: 170px;
    background: linear-gradient(90deg, var(--panel-white), var(--panel-grey));
  }
  .card--back .wood { top: 0; bottom: 0; right: 0; left: 170px; }
  .fish-photo {
    position: absolute;
    top: 60px;
    left: 80px;
    width: 60px;
    height: 240px;
    border-radius: 50% 50% 40% 40% / 30% 30% 20% 20%;
    background: linear-gradient(90deg, var(--fish-dark), var(--fish-silver) 45%, var(--panel-white));
  }
  .website {
    position: absolute;
    top: 40px;
    left: 38px;
    writing-mode: vertical-rl;
    font-weight: 300;
    font-size: 17px;
    color: var(--ink-dark);
    letter-spacing: 0.5px;
  }
  .back-logo {
    position: absolute;
    top: 90px;
    left: 225px;
    writing-mode: vertical-rl;
    font-weight: 700;
    font-size: 50px;
    line-height: 1;
    color: var(--logo-blue);
  }
</style>
</head>
<body>
<main class="canvas">
  <section class="card card--front" aria-label="Business card front">
    <div class="wood" role="img" aria-label="Grey weathered timber planks"></div>
    <div class="front-logo">Harbour<br>Fillet Co</div>
    <ul class="contact">
      <li class="contact__name">Liam Carter</li>
      <li>
        <svg viewBox="0 0 12 12" aria-hidden="true"><rect x="1" y="1" width="10" height="10" rx="2" fill="#fff"/><path d="M4 3.5c0 2.5 2 4.5 4.5 4.5l.5-1.5-1.5-.5-.7.6C5.9 6.2 5.6 5.8 5.4 5l.6-.7L5.5 3z" fill="#777"/></svg>
        0000-000-000
      </li>
      <li>
        <svg viewBox="0 0 12 12" aria-hidden="true"><rect x="1" y="2.5" width="10" height="7" fill="#fff"/><path d="M1 2.5l5 4 5-4" stroke="#777" fill="none"/></svg>
        hello@harbourfillet.com.au
      </li>
      <li>
        <svg viewBox="0 0 12 12" aria-hidden="true"><path d="M6 11S2 6.8 2 4.5a4 4 0 0 1 8 0C10 6.8 6 11 6 11z" fill="#fff"/><circle cx="6" cy="4.5" r="1.4" fill="#777"/></svg>
        Shop 7/210-236 Wattlebay Rd,
      </li>
      <li>Kirrawee 4812</li>
    </ul>
    <div class="dish-photo" role="img" aria-label="Grilled salmon fillets with lemon slices and green beans on a white plate"></div>
  </section>

  <section class="card card--back" aria-label="Business card back">
    <div class="info-panel">
      <div class="fish-photo" role="img" aria-label="Photograph of a whole Atlantic salmon"></div>
      <div class="website">www.harbourfilletco.com.au</div>
    </div>
    <div class="wood" role="img" aria-label="Grey weathered timber planks"></div>
    <div class="back-logo">Harbour Fillet Co</div>
  </section>
</main>
</body>
</html>
```